New menu rebranding for Asian fusion

I have my current menu attached, but I want to change it and make it more attractive. The restaurant is an Asian Fusion. Food from Thailand, China, Japan, Indonesia, Malaysia, Cambodia. We cater to mid to high end consumers with an educated and sophisticated pallet. Maybe try a modern twist, or an authentic variation, maybe a mix. Please don't play with the logo too much, but feel free to play with the pattern. I also want to have as many pictures of dishes visible as possible. Additionally, keep in mind that the menu will be in two languages, so please design accordingly. Feel free to play around with the format of the menu and the logo too if you get carried away. Keep it in mind that this is also a take out menu too. Please check out the Instagram account lotus_crate As well as facebook etc. Let me know if you need any additional files. Thx and appreciated.
Updates

I have made an update to the Menu. It's not the original file. It's smaller now. Please see the attached PDF file. Best regards, Added Monday, February 02, 2015

Target Market(s)

Mid to high end

Industry/Entity Type

Restaurant

Number of Pages Required

3 page

Requirements
Must have
• dual language friendly. At least make space for it.
• Must keep logo.
Nice to have
• Would be nice to stick to same theme, not too much change to branding.

```html
<!DOCTYPE html>
<html lang="en">
<head>
<meta charset="utf-8">
<title>Main Menu</title>
<link rel="stylesheet" href="https://fonts.googleapis.com/css2?family=Michroma&family=Exo+2:wght@400;600&family=Noto+Naskh+Arabic:wght@400&display=swap">
<style>
  :root {
    --stage: #8d8d8d;
    --page: #161616;
    --page-deep: #0c0c0c;
    --accent: #e2661b;
    --accent-dark: #c95514;
    --ink: #ffffff;
    --table-light: #e6e6e6;
    --table-mid: #9a9a9a;
    --table-dark: #6f6f6f;
    --table-darker: #4a4a4a;
  }
  * { box-sizing: border-box; margin: 0; padding: 0; }
  html, body { width: 1200px; height: 800px; overflow: hidden; }
  body {
    background: var(--stage);
    font-family: "Exo 2", sans-serif;
    color: var(--ink);
    position: relative;
  }
  .page {
    position: absolute;
    top: 20px;
    width: 560px;
    height: 760px;
    background: linear-gradient(180deg, #1d1d1d 0%, var(--page) 50%, var(--page-deep) 100%);
    overflow: hidden;
  }
  .page--left { left: 30px; }
  .page--right { left: 610px; }

  .menu-banner {
    position: absolute;
    background: var(--accent);
    display: flex;
    align-items: center;
    justify-content: center;
    font-family: "Michroma", sans-serif;
    font-size: 19px;
    color: var(--ink);
  }
  .page--left .menu-banner { left: 20px; top: 20px; width: 200px; height: 110px; }
  .page--right .menu-banner { left: 20px; top: 20px; width: 190px; height: 86px; }

  .section-title {
    position: absolute;
    font-family: "Michroma", sans-serif;
    font-size: 16px;
    display: flex;
    align-items: center;
    gap: 10px;
  }
  .section-title::after {
    content: "";
    height: 1px;
    width: 60px;
    background: #bdbdbd;
    margin-top: 8px;
  }

  /* main dishes grid */
  .dish-grid {
    position: absolute;
    left: 20px;
    top: 138px;
    display: grid;
    grid-template-columns: repeat(4, 123px);
    grid-auto-rows: 120px;
    gap: 8px;
  }
  .dish {
    position: relative;
    overflow: hidden;
  }
  .dish__photo { position: absolute; inset: 0; }
  .dish__price {
    position: absolute;
    top: 0; right: 0;
    width: 34px;
    background: var(--accent);
    font-family: "Michroma", sans-serif;
    font-size: 9px;
    line-height: 1.15;
    text-align: center;
    padding: 3px 0;
  }
  .dish__price b { display: block; font-size: 12px; font-weight: 400; }
  .dish__name {
    position: absolute;
    left: 8px; bottom: 6px; right: 8px;
    font-family: "Michroma", sans-serif;
    font-size: 8.5px;
    line-height: 1.25;
    text-shadow: 0 1px 2px #000;
  }
  .dish__name span {
    display: block;
    font-family: "Noto Naskh Arabic", serif;
    font-size: 9px;
    direction: rtl;
    text-align: left;
  }
  .hero-photo {
    position: absolute;
    left: 0; top: 525px;
    width: 560px; height: 235px;
    background: radial-gradient(ellipse at 45% 45%, #8a5a2a 0%, #5a3518 35%, #2a1a0e 65%, #e8e8e8 66%, #cfcfcf 75%, #1a1a1a 100%);
  }

  /* right page */
  .photo-column {
    position: absolute;
    left: 20px; top: 120px;
    display: grid;
    grid-template-columns: repeat(2, 105px);
    grid-auto-rows: 110px;
    gap: 8px;
  }
  .photo-tile { width: 100%; height: 100%; }

  .price-list {
    position: absolute;
    left: 250px;
    display: flex;
    gap: 6px;
  }
  .price-list__names, .price-list__prices {
    background: var(--accent);
    font-family: "Michroma", sans-serif;
    font-size: 7.5px;
    line-height: 13px;
    padding: 6px 8px;
    list-style: none;
  }
  .price-list__names { width: 206px; }
  .price-list__prices { width: 66px; text-align: center; }

  .lunch {
    position: absolute;
    left: 20px; top: 500px;
    width: 340px;
  }
  .lunch__title {
    background: var(--accent);
    font-family: "Michroma", sans-serif;
    font-size: 15px;
    text-align: center;
    height: 30px;
    line-height: 30px;
  }
  .lunch__table {
    width: 100%;
    border-collapse: collapse;
    font-family: "Michroma", sans-serif;
    font-size: 7px;
  }
  .lunch__table th, .lunch__table td { height: 16px; text-align: center; font-weight: 400; }
  .lunch__table thead th { background: var(--table-darker); }
  .lunch__table th.dish-col { background: var(--table-light); color: #333; }
  .lunch__table td.dish-col { background: var(--table-light); color: var(--accent); text-align: left; padding-left: 10px; width: 42%; }
  .lunch__table td:nth-child(2) { background: var(--table-mid); }
  .lunch__table td:nth-child(3) { background: var(--table-dark); }
  .lunch__table td:nth-child(4) { background: var(--table-mid); }
  .lunch__table td:nth-child(5) { background: var(--table-dark); }
  .lunch__table td:nth-child(6) { background: var(--table-darker); }

  .side-photo { position: absolute; left: 372px; width: 168px; }
</style>
</head>
<body>

<section class="page page--left">
  <div class="menu-banner">Main Menu</div>
  <h2 class="section-title" style="left:232px; top:100px;">Main Dishes</h2>

  <div class="dish-grid">
    <article class="dish">
      <div class="dish__photo" role="img" aria-label="Photo of orange chicken on a white plate" style="background:radial-gradient(circle at 50% 55%, #d2801f, #6b3a10 55%, #222 100%);"></div>
      <div class="dish__price">RS.<b>33</b></div>
      <p class="dish__name">Orange Chicken<span>دجاج البرتقال</span></p>
    </article>
    <article class="dish">
      <div class="dish__photo" role="img" aria-label="Photo of chicken teriyaki" style="background:radial-gradient(circle at 50% 50%, #6a2a3a, #3a1820 55%, #d8d8d8 100%);"></div>
      <div class="dish__price">RS.<b>34</b></div>
      <p class="dish__name">Chicken Teriyaki<span>دجاج ترياكي</span></p>
    </article>
    <article class="dish">
      <div class="dish__photo" role="img" aria-label="Photo of beef with broccoli in a takeout box" style="background:radial-gradient(circle at 50% 50%, #4a3a1a, #2e4a1e 50%, #111 100%);"></div>
      <div class="dish__price">RS.<b>41</b></div>
      <p class="dish__name">Beef Broccoli<span>لحم مع بروكلي</span></p>
    </article>
    <article class="dish">
      <div class="dish__photo" role="img" aria-label="Photo of szechuan beef" style="background:radial-gradient(circle at 50% 50%, #5a3a18, #2a1a0c 60%, #111 100%);"></div>
      <div class="dish__price">RS.<b>43</b></div>
      <p class="dish__name">Szechuan Beef<span>لحم سيشوان</span></p>
    </article>
    <article class="dish">
      <div class="dish__photo" role="img" aria-label="Photo of rendang beef in a bowl" style="background:radial-gradient(circle at 50% 50%, #6a4028, #3a2418 55%, #151515 100%);"></div>
      <div class="dish__price">RS.<b>43</b></div>
      <p class="dish__name">Rendang Beef<span>لحم رندانغ</span></p>
    </article>
    <article class="dish">
      <div class="dish__photo" role="img" aria-label="Photo of mongolian beef with green onions" style="background:radial-gradient(circle at 50% 50%, #3a4a2a, #2a2018 55%, #111 100%);"></div>
      <div class="dish__price">RS.<b>42</b></div>
      <p class="dish__name">Mongolian Beef<span>لحم منغولي</span></p>
    </article>
    <article class="dish">
      <div class="dish__photo" role="img" aria-label="Photo of himalayan beef with fresh greens" style="background:radial-gradient(circle at 50% 50%, #5a2a30, #2e3a20 55%, #e0e0e0 100%);"></div>
      <div class="dish__price">RS.<b>43</b></div>
      <p class="dish__name">Himalayan Beef</p>
    </article>
    <article class="dish">
      <div class="dish__photo" role="img" aria-label="Photo of shrimp teppanyaki" style="background:radial-gradient(circle at 50% 50%, #b0502a, #5a2a18 55%, #1a1a1a 100%);"></div>
      <div class="dish__price">RS.<b>41</b></div>
      <p class="dish__name">Shrimp Teppanyaki<span>جمبري تبانياكي</span></p>
    </article>
    <article class="dish">
      <div class="dish__photo" role="img" aria-label="Photo of sweet and sour shrimp" style="background:radial-gradient(circle at 50% 45%, #d0703a, #6a6a8a 55%, #222 100%);"></div>
      <div class="dish__price">RS.<b>43</b></div>
      <p class="dish__name">Sweet n Sour Shrimp</p>
    </article>
    <article class="dish">
      <div class="dish__photo" role="img" aria-label="Photo of fried shrimp balls in a bowl" style="background:radial-gradient(circle at 50% 50%, #e09040, #7a4a1a 50%, #1a1a1a 100%);"></div>
      <div class="dish__price">RS.<b>55</b></div>
      <p class="dish__name">Ball Shrimp</p>
    </article>
    <article class="dish">
      <div class="dish__photo" role="img" aria-label="Photo of fried fish balls" style="background:radial-gradient(circle at 50% 50%, #d88a3a, #6a3a18 50%, #151515 100%);"></div>
      <div class="dish__price">RS.<b>50</b></div>
      <p class="dish__name">Ball Fish</p>
    </article>
    <article class="dish">
      <div class="dish__photo" role="img" aria-label="Photo of fish sambal in a white bowl" style="background:radial-gradient(circle at 50% 50%, #c0502a, #e8e0d8 55%, #2a2a2a 100%);"></div>
      <div class="dish__price">RS.<b>55</b></div>
      <p class="dish__name">Fish Sambal</p>
    </article>
  </div>

  <div class="hero-photo" role="img" aria-label="Large photo of glazed crispy chicken topped with spring onions on a white plate"></div>
</section>

<section class="page page--right">
  <div class="menu-banner">Main Menu</div>

  <div class="photo-column">
    <div class="photo-tile" role="img" aria-label="Photo of chicken satay skewers" style="background:linear-gradient(135deg,#5a6a7a,#8a7a5a 60%,#2a2a2a);"></div>
    <div class="photo-tile" role="img" aria-label="Photo of tom yum soup" style="background:radial-gradient(circle,#c0602a,#6a2a18 55%,#1a1a1a);"></div>
    <div class="photo-tile" role="img" aria-label="Photo of a curry bowl with vegetables" style="background:radial-gradient(circle,#d8b060,#5a4a2a 55%,#111);"></div>
    <div class="photo-tile" role="img" aria-label="Photo of stir-fried noodles" style="background:radial-gradient(circle,#b08a50,#4a3a22 60%,#151515);"></div>
    <div class="photo-tile" role="img" aria-label="Photo of a fresh salad" style="background:radial-gradient(circle,#8aa06a,#4a5a6a 60%,#1a2030);"></div>
    <div class="photo-tile" role="img" aria-label="Photo of a soup bowl with dipping sauce" style="background:radial-gradient(circle,#d8d0b0,#5a7a9a 60%,#1a2a3a);"></div>
  </div>

  <h2 class="section-title" style="left:225px; top:108px;">Starters</h2>
  <div class="price-list" style="top:138px;">
    <ul class="price-list__names">
      <li>Tom Yum Soup</li><li>Chicken Satay</li><li>Spring Rolls</li><li>Dim Dim</li>
      <li>Edamame</li><li>Crispy Tofu with peanuts</li><li>Dynamite Shrimp</li>
    </ul>
    <ul class="price-list__prices">
      <li>RS. 21</li><li>RS. 34</li><li>RS. 22</li><li>RS. 11</li>
      <li>RS. 34</li><li>RS. 55</li><li>RS. 55</li>
    </ul>
  </div>

  <h2 class="section-title" style="left:225px; top:278px;">Salads</h2>
  <div class="price-list" style="top:306px;">
    <ul class="price-list__names">
      <li>Thai Beef Salad</li><li>Thai Shrimp Salad</li><li>Gado Gado</li><li>Chinese Salad</li>
    </ul>
    <ul class="price-list__prices">
      <li>RS. 21</li><li>RS. 32</li><li>RS. 43</li><li>RS. 22</li>
    </ul>
  </div>

  <h2 class="section-title" style="left:225px; top:385px;">Side Dishes</h2>
  <div class="price-list" style="top:413px;">
    <ul class="price-list__names">
      <li>Steamed Rice</li><li>Fried Rice</li><li>Plain Noodles</li>
    </ul>
    <ul class="price-list__prices">
      <li>RS. 21</li><li>RS. 32</li><li>RS. 22</li>
    </ul>
  </div>

  <div class="lunch">
    <h2 class="lunch__title">Lunch Menu</h2>
    <table class="lunch__table">
      <thead>
        <tr><th class="dish-col">Main Dishes</th><th>Veg</th><th>Chicken</th><th>Beef</th><th>Shrimp</th><th>Fish</th></tr>
      </thead>
      <tbody>
        <tr><td class="dish-col">Pad Thai noodles</td><td>35</td><td>40</td><td>45</td><td>50</td><td>60</td></tr>
        <tr><td class="dish-col">Teriyaki Fried Rice</td><td>35</td><td>40</td><td>45</td><td>50</td><td>60</td></tr>
        <tr><td class="dish-col">Szechuan Noodles</td><td>35</td><td>40</td><td>45</td><td>50</td><td>60</td></tr>
        <tr><td class="dish-col">Sambal Fried Rice</td><td>35</td><td>40</td><td>45</td><td>50</td><td>60</td></tr>
        <tr><td class="dish-col">RedCurry Fried Rice</td><td>35</td><td>40</td><td>45</td><td>50</td><td>60</td></tr>
        <tr><td class="dish-col">Chow Mein Noodles</td><td>35</td><td>40</td><td>45</td><td>50</td><td>60</td></tr>
        <tr><td class="dish-col">Yakisoba noodles</td><td>35</td><td>40</td><td>45</td><td>50</td><td>60</td></tr>
        <tr><td class="dish-col">Thai Basil Fried Rice</td><td>35</td><td>40</td><td>45</td><td>50</td><td>60</td></tr>
      </tbody>
    </table>
  </div>

  <div class="side-photo" role="img" aria-label="Photo of a noodle salad with vegetables" style="top:500px; height:100px; background:radial-gradient(circle,#c08a4a,#5a6a3a 55%,#1a1a1a);"></div>
  <div class="side-photo" role="img" aria-label="Photo of a bowl of noodles" style="top:608px; height:92px; background:radial-gradient(circle,#d8c890,#6a7a5a 50%,#111);"></div>
</section>

</body>
</html>
```